Roadside building business signage for a holistic health clinic.

Replace signs as shown in the attached file. They are perforated stickers that go on the windows as shown. Looking for something that has our logo and says the name of the practice with logo (Fernbrook Health & Wellness) also boldly says Acupuncture, IV Vitamins, and Holistic Health.
Possibly our phone number as well 318-627-5194
Updates

Please don't use pink except the logo. Earthy, organic tone colors appreciated.

Need of eye catching window signage of a holistic clinic on a brick building. Pink, purple, sage green, white color. Logo is pink on a white background. Please don't overload with too much pink. Words to include are "Fernbrook Health and Wellness(name of business)", "Direct Primary Care", " Medical acupuncture", "IV Vitamin Therapy", "fernbrookcare-example.com","318-627-5194".

Target Market(s)

People will see in their cars passing by the building. Busy roadside so need to be visible while passing in fast speed.

Industry/Entity Type

Health & Wellness

Font styles to use
Sans Serif

Colors

Designer to choose colors to be used in the design.

Requirements
Must have
• On sign must have words Holistic Medicine, Medical Acupuncture, Direct Primary Care and IV vitamins.
Nice to have
• Simple, minimalistic, artistic yet has clear message. White, Black, Violet, Pink (logo), Dark green, Sage green.
Should not have
• Bold colors (red, yellow, blue), same tone colors. Blue waves on the current signage (uploaded file) must go.

```html
<!DOCTYPE html>
<html lang="en">
<head>
<meta charset="utf-8">
<title>Fernbrook Health &amp; Wellness – Window Signage Draft 4</title>
<link rel="stylesheet" href="https://fonts.googleapis.com/css2?family=Cinzel:wght@600;700&family=Oswald:wght@600&family=Arimo:wght@400&display=swap">
<style>
  :root {
    --board: #f1f1f1;
    --panel: #ffffff;
    --frame: #4a8fa8;
    --ink: #2a5f5c;
    --accent: #e07aa6;
    --note-band: #a8a8a8;
    --note-ink: #9a9a9a;
    --brick-top: #8d5a4c;
    --brick-mid: #7a4f45;
    --mulch: #4b3a33;
  }
  * { margin: 0; padding: 0; box-sizing: border-box; }
  html, body { width: 945px; height: 1200px; overflow: hidden; background: var(--board); }
  .board { position: relative; width: 945px; height: 1200px; }

  .window-layout { position: absolute; left: 0; top: 0; width: 945px; height: 560px; }
  .pane { fill: var(--panel); stroke: var(--frame); stroke-width: 1.2; }
  .divider { stroke: var(--frame); stroke-width: 1; }
  .label {
    font-family: "Cinzel", serif;
    font-weight: 700;
    fill: var(--ink);
    text-anchor: middle;
    letter-spacing: 1px;
  }
  .label--big { font-size: 16px; }
  .label--small { font-size: 12.5px; }
  .brand-name { font-family: "Cinzel", serif; font-weight: 600; font-size: 17px; fill: var(--ink); text-anchor: middle; }
  .brand-sub { font-family: "Cinzel", serif; font-weight: 600; font-size: 5.6px; letter-spacing: 2px; fill: var(--ink); text-anchor: middle; }
  .brand-dot { fill: var(--accent); }
  .phone { font-family: "Oswald", sans-serif; font-weight: 600; font-size: 24px; fill: var(--ink); text-anchor: middle; }

  .mockup-photo {
    position: absolute; left: 61px; top: 576px; width: 412px; height: 546px;
    background: linear-gradient(180deg, #c9d3da 0%, var(--brick-top) 12%, var(--brick-mid) 62%, #5f6e45 78%, var(--mulch) 100%);
  }

  .draft-tag {
    position: absolute; left: 674px; top: 946px; width: 271px; height: 61px;
    background: var(--note-band); color: #fff;
    font-family: "Arimo", sans-serif; font-size: 14.5px; line-height: 16px;
    padding: 6px 8px;
  }
  .design-notes {
    position: absolute; left: 682px; top: 1012px; width: 260px;
    font-family: "Arimo", sans-serif; font-size: 10.6px; line-height: 11.4px; color: var(--note-ink);
  }
  .design-notes p { margin-bottom: 11px; }
</style>
</head>
<body>
<main class="board">

  <svg class="window-layout" viewBox="0 0 945 560" role="img" aria-label="Flat layout of the window signs for Fernbrook Health and Wellness">
    <!-- arched top panes -->
    <path class="pane" d="M338 242 Q352 80 474 44 Q596 80 610 242 Z"/>
    <line class="divider" x1="474" y1="44" x2="474" y2="242"/>
    <g class="label label--big">
      <text x="413" y="158">FERNBROOK</text><text x="413" y="183">HEALTH</text><text x="413" y="207">AND</text><text x="413" y="232">WELLNESS</text>
      <text x="537" y="158">FERNBROOK</text><text x="537" y="183">HEALTH</text><text x="537" y="207">AND</text><text x="537" y="232">WELLNESS</text>
    </g>

    <!-- brand row -->
    <rect class="pane" x="202" y="242" width="136" height="135"/>
    <rect class="pane" x="338" y="242" width="136" height="135"/>
    <rect class="pane" x="474" y="242" width="136" height="135"/>
    <rect class="pane" x="610" y="242" width="137" height="135"/>
    <g>
      <circle class="brand-dot" cx="270" cy="294" r="14"/>
      <text class="brand-name" x="270" y="336" textLength="118" lengthAdjust="spacingAndGlyphs">FERNBROOK</text>
      <text class="brand-sub" x="270" y="348">HEALTH &amp; WELLNESS</text>
      <circle class="brand-dot" cx="406" cy="294" r="14"/>
      <text class="brand-name" x="406" y="336" textLength="118" lengthAdjust="spacingAndGlyphs">FERNBROOK</text>
      <text class="brand-sub" x="406" y="348">HEALTH &amp; WELLNESS</text>
      <circle class="brand-dot" cx="542" cy="294" r="14"/>
      <text class="brand-name" x="542" y="336" textLength="118" lengthAdjust="spacingAndGlyphs">FERNBROOK</text>
      <text class="brand-sub" x="542" y="348">HEALTH &amp; WELLNESS</text>
      <circle class="brand-dot" cx="679" cy="294" r="14"/>
      <text class="brand-name" x="679" y="336" textLength="118" lengthAdjust="spacingAndGlyphs">FERNBROOK</text>
      <text class="brand-sub" x="679" y="348">HEALTH &amp; WELLNESS</text>
    </g>

    <!-- services row -->
    <rect class="pane" x="65" y="377" width="137" height="134"/>
    <rect class="pane" x="202" y="377" width="136" height="134"/>
    <rect class="pane" x="338" y="377" width="136" height="134"/>
    <rect class="pane" x="474" y="377" width="136" height="134"/>
    <rect class="pane" x="610" y="377" width="137" height="134"/>

    <g class="label label--small">
      <text x="134" y="405">IV VITAMINS</text>
      <text x="134" y="430">HOLISTIC</text><text x="134" y="450">HEALTH</text>
      <text x="679" y="405">IV VITAMINS</text>
      <text x="679" y="430">HOLISTIC</text><text x="679" y="450">HEALTH</text>
      <text x="406" y="396">HOLISTIC</text><text x="406" y="415">MEDICINE</text>
      <text x="406" y="440">MEDICAL</text>
      <text x="406" y="460" textLength="124" lengthAdjust="spacingAndGlyphs">ACUPUNCTURE</text>
      <text x="406" y="486">DIRECT</text>
      <text x="406" y="505" textLength="124" lengthAdjust="spacingAndGlyphs">PRIMARY CARE</text>
    </g>
    <line class="divider" x1="72" y1="414" x2="196" y2="414"/>
    <line class="divider" x1="72" y1="466" x2="196" y2="466"/>
    <line class="divider" x1="618" y1="414" x2="741" y2="414"/>
    <line class="divider" x1="617" y1="466" x2="741" y2="466"/>
    <line class="divider" x1="345" y1="424" x2="468" y2="424"/>
    <line class="divider" x1="345" y1="470" x2="468" y2="470"/>
    <text class="phone" x="134" y="498" textLength="116" lengthAdjust="spacingAndGlyphs">318-627-5194</text>
    <text class="phone" x="679" y="498" textLength="116" lengthAdjust="spacingAndGlyphs">318-627-5194</text>

    <g class="label label--big">
      <text x="270" y="414" textLength="118" lengthAdjust="spacingAndGlyphs">FERNBROOK</text><text x="270" y="439">HEALTH</text><text x="270" y="463">AND</text><text x="270" y="488">WELLNESS</text>
      <text x="542" y="414" textLength="118" lengthAdjust="spacingAndGlyphs">FERNBROOK</text><text x="542" y="439">HEALTH</text><text x="542" y="463">AND</text><text x="542" y="488">WELLNESS</text>
    </g>
  </svg>

  <div class="mockup-photo" role="img" aria-label="Photo mockup: the window signs applied to the arched corner windows of the brick clinic building, with shrubs and mulch in front"></div>

  <div class="draft-tag">DRAFT 4:<br>Fourth version for proof of concept and the 4th round of feedback</div>
  <div class="design-notes">
    <p>Concept Design Description:<br>Using blue for the windows<br>(metal frame kept unchanged)</p>
    <p>To keep the central 4 squares in white<br>for the logo and the text to pop</p>
    <p>The use of a sky pattern for the windows<br>to bring serenity while also having something<br>visually attention grabbing</p>
  </div>

</main>
</body>
</html>
```